Marty Fernhollow SUP Boards

We are a 100% owned and operated Australian Stand Up Paddle Board company, specialising in online sales of Stand Up Paddle Board packages.

We want our website to have an ocean, sunset, beach warm feel.

We sell 4 packages and need to be able to edit content and upload a number of photos of each package for sale.

Customers will be able to email us to receive quotes on freight costs and then pay via Tendro only. We will have a Loopwall page and Brinvale adds that need to be linked to the website also.

Target Market(s)

Surfers and Stand up paddle boarders

Industry/Entity Type

It Company

Number of Pages Required

3 page

Requirements
Must have
• Link to Tendro for payment
• Link to Loopwall page
• Three tabs- Welcome page, SUP Boards and a Contact us page

```html
<!DOCTYPE html>
<html lang="en">
<head>
<meta charset="utf-8">
<title>Marty Fernhollow SUP Boards</title>
<link rel="stylesheet" href="https://fonts.googleapis.com/css2?family=Open+Sans:wght@700;800&family=Oswald:wght@400&display=swap">
<style>
  :root {
    --topbar: #2a2a2a;
    --sky-top: #8fa5b3;
    --sky-mid: #e2b878;
    --sky-glow: #ee8a3c;
    --sea: #6d727e;
    --sand-dark: #2b2f3d;
    --accent: #f5a01e;
    --button: #e8650f;
    --button-edge: #b84c08;
    --logo-ink: #1e1a12;
    --divider: #f2f2f2;
    --lower-bg: #9aa096;
    --panel: #d6d9d0;
    --panel-ink: #4a4a48;
    --white: #ffffff;
  }
  * { margin: 0; padding: 0; box-sizing: border-box; }
  html, body { width: 1200px; height: 1000px; overflow: hidden; background: var(--white); }
  body { position: relative; font-family: "Open Sans", Arial, sans-serif; }

  .top-bar { position: absolute; left: 0; top: 0; width: 1200px; height: 7px; background: var(--topbar); }

  .hero { position: absolute; left: 0; top: 7px; width: 1200px; height: 824px; overflow: hidden; }
  .hero-photo {
    position: absolute; inset: 0;
    background:
      radial-gradient(ellipse 420px 70px at 615px 385px, rgba(255,150,60,0.75), rgba(255,150,60,0) 100%),
      linear-gradient(180deg,
        var(--sky-top) 0%, #bdb79c 14%, var(--sky-mid) 26%, #eba664 36%, var(--sky-glow) 44%, #e8772e 47%,
        #b9a79a 47.3%, #a39c98 52%, var(--sea) 60%, #555a68 66%,
        #9a7a5e 69%, #6e5e58 74%, var(--sand-dark) 80%, #232634 100%);
  }
  .brand {
    position: absolute; left: 0; right: 0; top: 110px; text-align: center;
    font-size: 40px; font-weight: 800; color: var(--logo-ink); letter-spacing: -0.5px; line-height: 54px;
  }
  .hero-tagline {
    position: absolute; left: 0; right: 0; top: 698px; text-align: center;
    font-size: 26px; line-height: 34px; font-weight: 700; color: var(--accent); letter-spacing: 0.5px;
  }
  .products-button {
    position: absolute; left: 565px; top: 740px; width: 91px; height: 32px;
    background: var(--button); border-bottom: 2px solid var(--button-edge); border-radius: 2px;
    color: var(--white); font-family: Arial, Helvetica, sans-serif; font-weight: 700; font-size: 15px;
    line-height: 30px; text-align: center; text-decoration: none;
  }
  .badge {
    position: absolute; left: 15px; top: 718px; width: 78px; height: 78px;
    border-radius: 50%; background: #cfc6b4; border: 2px solid #e6e0d2;
  }

  .divider { position: absolute; left: 0; top: 831px; width: 1200px; height: 3px; background: var(--divider); }

  .package { position: absolute; left: 0; top: 834px; width: 1200px; height: 166px; overflow: hidden;
    background: linear-gradient(180deg, #8e958a 0%, var(--lower-bg) 60%, #b3b5a6 100%); }
  .package-photo {
    position: absolute; left: 35px; top: 32px; width: 420px; height: 140px;
    background: linear-gradient(90deg, #c9a774 0%, #c9a774 36%, #8e958a 40%, #2e2e32 44%, #2e2e32 76%, #8e958a 80%);
    border-radius: 70px 70px 0 0;
  }
  .package-panel {
    position: absolute; left: 497px; top: 91px; width: 697px; height: 90px;
    background: var(--panel);
  }
  .package-title {
    position: absolute; left: 32px; top: 28px;
    font-family: "Oswald", "Arial Narrow", sans-serif; font-weight: 400; font-size: 42px;
    color: var(--panel-ink); line-height: 1;
  }
</style>
</head>
<body>
  <div class="top-bar"></div>

  <header class="hero">
    <div class="hero-photo" role="img" aria-label="Sunset over the ocean with a paddle boarder walking along the beach carrying a board"></div>
    <div class="brand">Marty Fernhollow SUP Boards</div>
    <div class="badge" role="img" aria-label="Round badge"></div>
    <h1 class="hero-tagline">Choose Your Package, And Start Paddling</h1>
    <a class="products-button" href="#packages">Products</a>
  </header>

  <div class="divider"></div>

  <section class="package" id="packages">
    <div class="package-photo" role="img" aria-label="Bamboo stand up paddle board with board bag and paddle"></div>
    <div class="package-panel">
      <h2 class="package-title">PACKAGE 2</h2>
    </div>
  </section>
</body>
</html>
```